creation of business cards for Velanto Sàrl

Velanto S% 26 # 224; rl is a soci% 26 # 233; t% 26 # 233; consultancy that accompanies companies in the development of their business on the market% 26 # 233; Switzerland by providing strategic contacts or market information; and by providing administrative or logistical support. Our consulting skills focus on sectors% 26 # 224; high value added% 26 # 233; e, such as trade in food goods% 26 # 39amp; drinks, fashion% 26amp; lifestyle, products and services for% 26 # 233; s in high-tech industries (pharmaceutical, chemical, m% 26 # 233; pricy 26% 23 #; cision) or sustainable solutions (% 26 # 233; energies renewable, mat% 26 # 233; recyclable materials). As part of the launch of our activity% 26 # 233;, we need% 26 # 39;% 26 # 233; to establish business cards to d% 26 # 233; work our new customers (Swiss or international).

Target Market(s)

Companies wishing to develop their activity% 26 # 233; s in Switzerland or% 26 # 224; l% 26 # 39;% 26 # 233; abroad (mainly in Europe).

Contact Information for Business Card

Prénom NOM
Velanto Sàrl
Bureau de Marvoisin
Rue des Tilleuls 47, 1870 Corvalle
Tél. : 032 718 46 39
info@velanto-example.ch
www.velanto-example.ch

Font styles to use
Serif
Sans Serif

Colors

Designer to choose colors to be used in the design.

Requirements
Must have
• The logo The name of the company% 26 # 233; t% 26 # 233; (Velanto S% 26 # 224; rl) One field for the mailing address One field for the number% 26 # 233; ro de t% 26 # 233; l% 26 # 233; phone One field for the % 26 # 39; email address and website

```html
<!DOCTYPE html>
<html lang="fr">
<head>
<meta charset="utf-8">
<title>Velanto Sàrl – cartes de visite</title>
<link href="https://fonts.googleapis.com/css2?family=Lato:wght@300;400;900&display=swap" rel="stylesheet">
<style>
  :root {
    --backdrop: #2b2c2e;
    --brand-blue: #0b4a63;
    --brand-blue-soft: #0f5470;
    --paper: #ffffff;
    --mist: #e4e9ec;
    --ink-grey: #5d6468;
    --ink-blue: #0b4a63;
  }
  * { margin: 0; padding: 0; box-sizing: border-box; }
  html, body { width: 1200px; height: 900px; overflow: hidden; }
  body {
    background: var(--backdrop);
    font-family: "Lato", sans-serif;
    position: relative;
  }
  .card {
    position: absolute;
    left: 290px;
    width: 620px;
    height: 360px;
    border-radius: 18px;
    overflow: hidden;
  }
  .card--front { top: 75px; background: var(--brand-blue); }
  .card--back { top: 465px; background: var(--paper); }

  .front-pattern {
    position: absolute;
    inset: 0;
    background: linear-gradient(135deg, var(--brand-blue-soft), var(--brand-blue));
  }
  .front-brand {
    position: absolute;
    left: 230px;
    top: 170px;
    display: flex;
    align-items: center;
    gap: 22px;
  }
  .brand-square {
    width: 60px;
    height: 60px;
    border-radius: 14px;
    flex: none;
  }
  .front-brand .brand-square { background: var(--paper); }
  .brand-name {
    font-weight: 300;
    font-size: 50px;
    letter-spacing: 6px;
    line-height: 1;
  }
  .front-brand .brand-name { color: var(--paper); }

  .back-decoration {
    position: absolute;
    right: 40px;
    top: 110px;
    width: 250px;
    height: 210px;
    border-radius: 52px;
    background: var(--mist);
  }
  .back-brand {
    position: absolute;
    left: 38px;
    top: 40px;
    display: flex;
    align-items: center;
    gap: 22px;
  }
  .back-brand .brand-square { background: var(--brand-blue); width: 56px; height: 56px; border-radius: 13px; }
  .back-brand .brand-name { color: var(--ink-blue); font-size: 46px; }

  .contact {
    position: absolute;
    left: 60px;
    top: 135px;
    color: var(--ink-grey);
    font-size: 16px;
    line-height: 1.35;
  }
  .contact__company {
    color: var(--ink-blue);
    font-weight: 900;
    font-size: 26px;
    margin-bottom: 2px;
  }
  .contact__office { margin-bottom: 10px; }
  .contact__address { margin-bottom: 10px; }
  .contact__list { list-style: none; }
  .contact__list li { display: flex; align-items: center; gap: 10px; height: 23px; }
  .contact__list svg { width: 15px; height: 15px; flex: none; }
</style>
</head>
<body>

  <section class="card card--front">
    <div class="front-pattern" role="img" aria-label="Motif répété de tuiles du symbole de la marque, bleu sur bleu"></div>
    <div class="front-brand">
      <span class="brand-square"></span>
      <span class="brand-name">VELANTO</span>
    </div>
  </section>

  <section class="card card--back">
    <div class="back-decoration"></div>
    <div class="back-brand">
      <span class="brand-square"></span>
      <span class="brand-name">VELANTO</span>
    </div>
    <div class="contact">
      <p class="contact__company">Velanto Sàrl</p>
      <p class="contact__office">Bureau de Marvoisin</p>
      <p class="contact__address">Rue des Tilleuls 47,<br>1870 Corvalle</p>
      <ul class="contact__list">
        <li>
          <svg viewBox="0 0 16 16" aria-hidden="true"><path d="M3 1.5l3 3-1.6 1.8c.9 1.9 2.4 3.4 4.3 4.3L10.5 9l3 3-1.8 2.3C6.7 14 2 9.3 1.7 4.3z" fill="#0b4a63"/></svg>
          <span>032 718 46 39</span>
        </li>
        <li>
          <svg viewBox="0 0 16 16" aria-hidden="true"><rect x="1" y="3" width="14" height="10" fill="#0b4a63"/><path d="M1.5 3.5L8 9l6.5-5.5" stroke="#fff" stroke-width="1.2" fill="none"/></svg>
          <span>info@velanto-example.ch</span>
        </li>
        <li>
          <svg viewBox="0 0 16 16" aria-hidden="true"><circle cx="8" cy="8" r="6.5" fill="none" stroke="#0b4a63" stroke-width="1.4"/><ellipse cx="8" cy="8" rx="2.8" ry="6.5" fill="none" stroke="#0b4a63" stroke-width="1.1"/><path d="M1.5 8h13M2.5 5h11M2.5 11h11" stroke="#0b4a63" stroke-width="1"/></svg>
          <span>www.velanto-example.ch</span>
        </li>
      </ul>
    </div>
  </section>

</body>
</html>
```